Lantern Advisory Business Cards

We need a new layout for our business cards. We have a logo already. But we might be interested in only using the Lantern portion of the logo. It has been uploaded.

We would like cards that are not overly busy. Clean. Modern. Perhaps a gray color for one side.

On the back, we would like to have the lantern part of the logo and "Step Forward, we're with you!"

Our business provides medics and safety training for corporate clients. Our website is www.lanternadvisoryllc.example.

Industry/Entity Type

Business

Contact Information for Business Card

We want include name, email address, cell phone, main line number, and website URL on the front. Use the following as an example: Marla Tobin, marla@lanternadvisoryllc.example, 402.318.7264 (cell), 402.947.315, and www.lanternadvisoryllc.example.

Font styles to use
Serif
Sans Serif

Requirements
Must have
• All required information. Back side logo with "Take the leap, we will catch you!"
Nice to have
• If possible, we would like to consider creating a card in a non-standard shape. Perhaps, the shape of a lantern. Just interested in understanding the option.

```html
<!DOCTYPE html>
<html lang="en">
<head>
<meta charset="UTF-8">
<title>Lantern Advisory Business Cards</title>
<link rel="stylesheet" href="https://fonts.googleapis.com/css2?family=Open+Sans:wght@400;600;700&display=swap">
<style>
  :root {
    --page-bg: #ecebe8;
    --card-bg: #ffffff;
    --brand-blue: #114b9c;
    --ink: #1d1d1d;
    --ink-soft: #2a2a2a;
    --card-shadow: rgba(0, 0, 0, 0.18);
  }
  * { margin: 0; padding: 0; box-sizing: border-box; }
  html, body {
    width: 1200px;
    height: 900px;
    overflow: hidden;
    background: var(--page-bg);
    font-family: "Open Sans", Arial, sans-serif;
  }
  .sheet {
    position: relative;
    width: 1200px;
    height: 900px;
  }
  .card {
    position: absolute;
    width: 630px;
    height: 360px;
    background: var(--card-bg);
    box-shadow: 0 10px 24px var(--card-shadow);
    overflow: hidden;
  }
  .card--back { left: 90px; top: 60px; }
  .card--front { left: 480px; top: 480px; }

  /* Back side */
  .back-mark {
    position: absolute;
    left: 0;
    right: 0;
    top: 92px;
    display: flex;
    align-items: center;
    justify-content: center;
    gap: 12px;
  }
  .back-mark__dot {
    width: 22px;
    height: 22px;
    border-radius: 50%;
    background: var(--brand-blue);
  }
  .back-mark__name {
    font-weight: 600;
    font-size: 26px;
    color: var(--brand-blue);
    letter-spacing: 0.5px;
  }
  .tagline-band {
    position: absolute;
    left: 0;
    right: 0;
    top: 210px;
    height: 70px;
    background: var(--brand-blue);
    display: flex;
    align-items: center;
    justify-content: center;
  }
  .tagline-band__text {
    color: #ffffff;
    font-weight: 700;
    font-size: 22px;
  }

  /* Front side */
  .contact {
    position: absolute;
    left: 310px;
    top: 48px;
  }
  .contact__name {
    color: var(--brand-blue);
    font-weight: 700;
    font-size: 21px;
    margin-bottom: 16px;
  }
  .contact__list { list-style: none; }
  .contact__item {
    display: flex;
    align-items: center;
    gap: 9px;
    font-size: 14.5px;
    color: var(--ink-soft);
    line-height: 22px;
  }
  .contact__icon {
    width: 13px;
    height: 13px;
    flex: none;
    fill: var(--brand-blue);
  }
  .front-mark {
    position: absolute;
    left: 46px;
    bottom: 60px;
    display: flex;
    align-items: center;
    gap: 12px;
  }
  .front-mark__dot {
    width: 20px;
    height: 20px;
    border-radius: 50%;
    background: var(--brand-blue);
  }
  .front-mark__name {
    font-weight: 600;
    font-size: 26px;
    color: var(--ink);
    letter-spacing: 0.5px;
  }
</style>
</head>
<body>
<main class="sheet">

  <section class="card card--back" aria-label="Card back">
    <div class="back-mark">
      <span class="back-mark__dot"></span>
      <span class="back-mark__name">Lantern Advisory</span>
    </div>
    <div class="tagline-band">
      <p class="tagline-band__text">Step Forward, we're with you!</p>
    </div>
  </section>

  <section class="card card--front" aria-label="Card front">
    <div class="contact">
      <h1 class="contact__name">Marla Tobin</h1>
      <ul class="contact__list">
        <li class="contact__item">
          <svg class="contact__icon" viewBox="0 0 16 16" aria-hidden="true"><path d="M4 1h8a1 1 0 0 1 1 1v12a1 1 0 0 1-1 1H4a1 1 0 0 1-1-1V2a1 1 0 0 1 1-1zm1 2v9h6V3H5zm3 10a.8.8 0 1 0 0 1.6A.8.8 0 0 0 8 13z"/></svg>
          402.318.7264
        </li>
        <li class="contact__item">
          <svg class="contact__icon" viewBox="0 0 16 16" aria-hidden="true"><path d="M3.6 1.2l2.2 2.6c.3.4.3.9 0 1.2L4.6 6.3c.9 2 2.5 3.7 4.6 4.7l1.3-1.2c.3-.3.9-.3 1.2 0l2.6 2.2c.4.3.4.9 0 1.3l-1.4 1.4c-.6.6-1.600.8-2.400.4C6 13.4 2.600 10 .9 5.5.6 4.700.8 3.800 1.400 3.200l1-1.900c.3-.4.9-.4 1.200-.1z"/></svg>
          402.947.315
        </li>
        <li class="contact__item">
          <svg class="contact__icon" viewBox="0 0 16 16" aria-hidden="true"><path d="M1 3h14v10H1V3zm1.5 1.2L8 8.4l5.5-4.2h-11zM2 5.4V12h12V5.4L8 10 2 5.4z"/></svg>
          marla@lanternadvisoryllc.example
        </li>
        <li class="contact__item">
          <svg class="contact__icon" viewBox="0 0 16 16" aria-hidden="true"><path d="M8 1a7 7 0 1 0 0 14A7 7 0 0 0 8 1zm-.8 1.8c-.6.7-1.3 1.6-1.3 2.4 0 .9 1.2 1 1.6 1.8.4.8-.2 1.7.4 2.5.5.6 1.5.4 1.6 1.4.1.8-.4 1.7-.6 2.2A5.4 5.4 0 0 1 7.2 2.8zm3.4 9.8c.2-.8.8-1.5.6-2.3-.2-.9-1.3-.9-1.6-1.8-.2-.7.6-1.3 1.3-1.5.6-.2 1.2.1 1.7.5a5.4 5.4 0 0 1-2 5.1z"/></svg>
          www.lanternadvisoryllc.example
        </li>
      </ul>
    </div>
    <div class="front-mark">
      <span class="front-mark__dot"></span>
      <span class="front-mark__name">Lantern Advisory</span>
    </div>
  </section>

</main>
</body>
</html>
```